Facebook, Twitter and Linkedin cover image design

Looking to update the facebook, twitter and aLinkedin cover images for Tandem Accounts . website www.tandacct.example
https://www.prolinknet.example/company/tandem-accounts-llc/mycompany/?viewAsMember=true
https://www.socialpage.example/tandacct
https://chirpline.example/tandacct

```html
<!DOCTYPE html>
<html lang="en">
<head>
<meta charset="utf-8">
<title>Tandem Accounts – Cover</title>
<link href="https://fonts.googleapis.com/css2?family=Montserrat:wght@500;600;800&display=swap" rel="stylesheet">
<style>
  :root {
    --brand-green: #4e8c3f;
    --panel-white: #ffffff;
    --headline-white: #ffffff;
    --headline-grey: #7b7b70;
    --body-grey: #6d6d64;
  }
  html, body {
    margin: 0;
    padding: 0;
    width: 1200px;
    height: 655px;
    overflow: hidden;
    background: var(--brand-green);
  }
  .cover {
    position: relative;
    width: 1200px;
    height: 655px;
    background: var(--brand-green);
    font-family: "Montserrat", Arial, sans-serif;
    overflow: hidden;
  }
  .cover__panel {
    position: absolute;
    inset: 0;
    width: 1200px;
    height: 655px;
  }
  .headline {
    position: absolute;
    top: 210px;
    margin: 0;
    font-weight: 800;
    font-size: 86px;
    line-height: 1;
    letter-spacing: -0.5px;
    white-space: nowrap;
  }
  .headline--lead {
    left: 168px;
    color: var(--headline-white);
  }
  .headline--tail {
    left: 577px;
    color: var(--headline-grey);
  }
  .sector-list {
    position: absolute;
    margin: 0;
    padding: 0;
    list-style: none;
    text-align: center;
    line-height: 29px;
  }
  .sector-list li { margin: 0; }
  .sector-list--left {
    left: 199px;
    width: 340px;
    top: 328px;
    font-size: 24.5px;
    color: var(--headline-white);
    font-weight: 600;
  }
  .sector-list--left li + li { margin-top: 27px; }
  .sector-list--right {
    left: 613px;
    width: 360px;
    top: 328px;
    font-size: 24.8px;
    color: var(--body-grey);
    font-weight: 500;
  }
  .sector-list--right li.sector--oil { margin-top: 27px; }
  .sector-list--right li.sector--transport { margin-top: 32px; }
</style>
</head>
<body>
  <main class="cover">
    <svg class="cover__panel" viewBox="0 0 1200 655" aria-hidden="true">
      <defs>
        <filter id="panel-shadow" x="-10%" y="-10%" width="120%" height="120%">
          <feDropShadow dx="0" dy="0" stdDeviation="6" flood-color="#000" flood-opacity="0.28"/>
        </filter>
      </defs>
      <polygon points="555,117 1034,211 1000,655 555,655" fill="#ffffff" filter="url(#panel-shadow)"/>
    </svg>

    <h1 class="headline headline--lead">Tandem</h1>
    <p class="headline headline--tail">Accounts</p>

    <ul class="sector-list sector-list--left">
      <li>Automotive &amp; Truck<br>Dealerships</li>
      <li>Repair, Parts &amp;<br>Tire Locations</li>
    </ul>

    <ul class="sector-list sector-list--right">
      <li>Manufacturing &amp;<br>Industrial Maintenance</li>
      <li class="sector--oil">Oil &amp; Gas</li>
      <li class="sector--transport">Transportation</li>
    </ul>
  </main>
</body>
</html>
```